Quarrybend Building Company / Website*

We need a design for a contracting company website based in KSA, something modern with the same color theme as the attached logo. including a page for people who want to submit their CV and try to apply for a job.Also to include the "about us, contact us, gallery, Divisions, Supplies, etc...". If possible to have an interactive or moving background. Please disregard the "Smart Solutions" Section in the attached profile.

Industry/Entity Type

Construction Company

Number of Pages Required

5+ page

Colors

Designer to choose colors to be used in the design.

Requirements
Must have
• Pages:
• about us, contact us, gallery, Divisions, Apply for a job, Supplies
Nice to have
• - Moving or interactive background

```html
<!DOCTYPE html>
<html lang="en">
<head>
<meta charset="utf-8">
<title>Quarrybend Building Company</title>
<link href="https://fonts.googleapis.com/css2?family=Mulish:wght@400;600;700&display=swap" rel="stylesheet">
<style>
:root{
  --orange:#f2a523;
  --brown:#2d221b;
  --ink:#2a2a2a;
  --muted:#555;
  --line:#d9d9d9;
  --white:#fff;
  --foot-text:#9c948c;
}
*{margin:0;padding:0;box-sizing:border-box}
html,body{width:1200px;height:3894px;overflow:hidden;background:var(--white)}
body{position:relative;font-family:"Mulish",sans-serif;color:var(--ink)}
.abs{position:absolute}
.center{left:0;width:1200px;text-align:center}
.btn{position:absolute;background:var(--orange);color:var(--ink);font-weight:700;font-size:15px;letter-spacing:.3px;display:flex;align-items:center;justify-content:center;text-transform:uppercase}
h2.title{position:absolute;left:0;width:1200px;text-align:center;font-weight:600;font-size:33px;letter-spacing:.3px;text-transform:uppercase;line-height:1}
.rule{position:absolute;left:540px;width:120px;height:3px;background:var(--orange)}
.para{position:absolute;left:144px;width:912px;text-align:center;font-size:17px;line-height:32px}

/* header */
.brand{left:144px;top:22px;display:flex;align-items:center;gap:12px}
.brand-mark{width:48px;height:72px;background:var(--orange)}
.brand-name{font-size:27px;font-weight:600;color:var(--ink);line-height:1.05;text-transform:uppercase}
.brand-name small{display:block;font-size:13px;font-weight:600;letter-spacing:.4px}
.phone{right:145px;top:27px;display:flex;align-items:center;gap:12px;font-size:24px}
.phone-badge{width:30px;height:30px;background:var(--orange);transform:rotate(45deg);display:flex;align-items:center;justify-content:center}
.nav{top:89px;font-size:14px;font-weight:600;text-transform:uppercase;transform:translateX(-50%);white-space:nowrap}
.nav.active::after{content:"";position:absolute;left:-4px;right:-4px;bottom:-8px;height:2px;background:var(--orange)}

/* hero */
.hero{top:134px;left:0;width:1200px;height:596px;clip-path:polygon(0 0,100% 0,100% 478px,50% 596px,0 483px);
  background:linear-gradient(180deg,#79c1dd 0%,#a6cfdc 22%,#c9b89a 40%,#a58a6a 65%,#6f6a63 100%)}
.hero-title{top:302px;color:var(--white);font-weight:700;font-size:33px;line-height:36px;text-shadow:0 2px 6px rgba(0,0,0,.45);text-transform:uppercase}
.diamond{position:absolute;width:42px;height:42px;background:var(--orange);transform:rotate(45deg)}
.diamond svg{position:absolute;left:9px;top:9px;transform:rotate(-45deg)}

/* bands */
.band{left:0;width:1200px;background:var(--brown)}
.band .title,.band .para{color:var(--white)}
.services{top:1115px;height:722px;clip-path:polygon(0 0,100% 0,100% 609px,50% 722px,0 609px)}
.card{position:absolute;top:302px;width:217px;height:216px;background:var(--white);text-align:center}
.card svg{position:absolute;left:74px;top:30px}
.card .bar{position:absolute;left:68px;top:132px;width:81px;height:3px;background:var(--orange)}
.card span{position:absolute;left:0;width:100%;top:153px;font-size:18px;font-weight:600;line-height:22px;text-transform:uppercase}
.chev{position:absolute}

/* projects */
.photo{position:absolute}

/* job */
.job{top:2528px;height:409px;clip-path:polygon(0 0,100% 0,100% 295px,50% 409px,0 295px)}
.upload{position:absolute;left:403px;top:230px;width:392px;height:59px;background:var(--white);display:flex;align-items:center;padding-left:18px;gap:10px;font-size:16px;color:#888}

/* partners */
.partner{position:absolute;width:168px;height:144px;border:1px solid var(--line);display:flex;align-items:center;justify-content:center}
.partner i{display:block;background:#c9c9c9}

/* footer */
.footer{top:3481px;height:413px;clip-path:polygon(50% 0,100% 112px,100% 100%,0 100%,0 112px);background:#1f1813}
.f-head{position:absolute;top:141px;color:var(--orange);font-size:16px;font-weight:600;text-transform:uppercase}
.f-list{position:absolute;top:168px;list-style:none;font-size:11px;color:var(--foot-text);line-height:19.5px}
.f-info{position:absolute;top:168px;list-style:none;font-size:11px;color:var(--foot-text);line-height:24.3px}
.f-info li{display:flex;align-items:center;gap:12px}
.f-info li b{display:inline-block;width:9px;height:9px;background:var(--foot-text);border-radius:2px}
.social{position:absolute;top:168px;width:42px;height:40px;border:1px solid #5a514a;display:flex;align-items:center;justify-content:center}
.social i{width:10px;height:10px;border-radius:50%;background:var(--foot-text)}
.f-brand{position:absolute;left:144px;top:140px;display:flex;align-items:center;gap:12px;color:var(--foot-text)}
.f-brand .brand-mark{background:#6a6059}
</style>
</head>
<body>

<!-- header -->
<div class="abs brand">
  <div class="brand-mark"></div>
  <div class="brand-name">Quarrybend<small>Building Company</small></div>
</div>
<div class="abs phone">
  <div class="phone-badge"><svg width="14" height="14" viewBox="0 0 24 24" style="transform:rotate(-45deg)"><path d="M6.6 10.8a15 15 0 0 0 6.6 6.6l2.2-2.2a1 1 0 0 1 1-.25 11.4 11.4 0 0 0 3.6.57 1 1 0 0 1 1 1V20a1 1 0 0 1-1 1A17 17 0 0 1 3 4a1 1 0 0 1 1-1h3.5a1 1 0 0 1 1 1c0 1.25.2 2.45.57 3.57a1 1 0 0 1-.25 1z" fill="#2a2a2a"/></svg></div>
  <span>+966 12 5550148</span>
</div>
<a class="abs nav active" style="left:469px">Home</a>
<a class="abs nav" style="left:567px">About Us</a>
<a class="abs nav" style="left:675px">Gallery</a>
<a class="abs nav" style="left:782px">Divisions</a>
<a class="abs nav" style="left:891px">Supplies</a>
<a class="abs nav" style="left:1009px">Contact Us</a>

<!-- hero -->
<div class="abs hero" role="img" aria-label="Aerial photo of a city skyline with modern towers under a blue sky"></div>
<div class="abs center hero-title">Phasellus consequat<br>sagittis suscipit</div>
<div class="btn" style="left:540px;top:391px;width:120px;height:43px">Read More</div>
<div class="diamond" style="left:45px;top:352px"><svg width="24" height="24" viewBox="0 0 24 24"><path d="M15 5l-7 7 7 7" stroke="#2a2a2a" stroke-width="3.5" fill="none"/></svg></div>
<div class="diamond" style="left:1106px;top:352px"><svg width="24" height="24" viewBox="0 0 24 24"><path d="M9 5l7 7-7 7" stroke="#2a2a2a" stroke-width="3.5" fill="none"/></svg></div>

<!-- welcome -->
<h2 class="title" style="top:806px">Welcome to Quarrybend Building Company</h2>
<div class="rule" style="top:857px"></div>
<p class="para" style="top:877px">QBC (Previously Al-Rawdan) was established in the year 1980 as a sub-contractor Specialized in waterproofing and speciali-zed finishing, with the main target of furnishing the Saudi market by a professional team of engineers and applicators to abide by the need of the fast-growing construction world in the Kingdom.</p>
<div class="btn" style="left:540px;top:993px;width:120px;height:42px">Read More</div>

<!-- services -->
<section class="abs band services">
  <h2 class="title" style="top:76px">Our Services</h2>
  <div class="rule" style="top:129px"></div>
  <p class="para" style="top:146px">Quarrybend Building Company (QBC) undertakes a range of civil works projects and takes pride in the safe, timely and cost effective delivery of civil construction projects in the Resources, Construction, Infrastructure, Utilities and Local Gover-nment sectors. Our highly skilled work crews work in conjunction with the client, offering integrated solutions to ensure the project scope is delivered safely, on time and within budget.</p>

  <div class="card" style="left:144px">
    <svg width="70" height="70" viewBox="0 0 70 70" fill="none" stroke="#2a2a2a" stroke-width="2"><path d="M6 4v62M6 8h56M12 8l-6 8M62 8v14M24 30h30v36H24zM30 38h6M42 38h6M30 48h6M42 48h6M30 58h6M42 58h6M2 66h66"/></svg>
    <div class="bar"></div><span>General<br>Contracting</span>
  </div>
  <div class="card" style="left:375px">
    <svg width="70" height="70" viewBox="0 0 70 70" fill="none" stroke="#2a2a2a" stroke-width="2"><path d="M20 6h30v60H20zM8 24h12v42H8zM50 30h12v36H50zM27 14h6M38 14h6M27 26h6M38 26h6M27 38h6M38 38h6M27 50h6M38 50h6M4 66h62"/></svg>
    <div class="bar"></div><span>Environmental<br>Works</span>
  </div>
  <div class="card" style="left:607px">
    <svg width="70" height="70" viewBox="0 0 70 70" fill="none" stroke="#2a2a2a" stroke-width="2"><path d="M27 8h16v12H27zM24 20h22M29 20l-12 46M41 20l12 46M25 36h20M21 52h28M25 36l24 16M45 36L21 52M10 66h50M35 2v6"/></svg>
    <div class="bar"></div><span>Marine Works</span>
  </div>
  <div class="card" style="left:839px">
    <svg width="70" height="70" viewBox="0 0 70 70" fill="none" stroke="#2a2a2a" stroke-width="2"><circle cx="20" cy="22" r="12"/><circle cx="30" cy="32" r="10"/><path d="M22 40v26M14 66h52M38 54h26M40 54v12M62 54v12M38 48h26M46 14a6 6 0 0 1 12 0 5 5 0 0 1 0 10H46a5 5 0 0 1 0-10z"/></svg>
    <div class="bar"></div><span>Landscape<br>Works</span>
  </div>
  <svg class="chev" style="left:53px;top:396px" width="22" height="32" viewBox="0 0 22 32"><path d="M16 4L6 16l10 12" stroke="#fff" stroke-width="4" fill="none"/></svg>
  <svg class="chev" style="left:1123px;top:396px" width="22" height="32" viewBox="0 0 22 32"><path d="M6 4l10 12-10 12" stroke="#fff" stroke-width="4" fill="none"/></svg>
  <div class="btn" style="left:508px;top:543px;width:183px;height:42px">View All Services</div>
</section>

<!-- projects -->
<h2 class="title" style="top:1906px">Projects</h2>
<div class="rule" style="top:1959px"></div>
<div class="photo" style="left:144px;top:1989px;width:296px;height:390px;background:linear-gradient(180deg,#2f6fb3,#5b84ad 55%,#8f8f8a)" role="img" aria-label="Tall glass towers under construction with cranes against a blue sky"></div>
<div class="photo" style="left:452px;top:1989px;width:295px;height:189px;background:linear-gradient(180deg,#3c64a8,#6e87b0 60%,#b8ad94)" role="img" aria-label="Blue glass office building under a clear sky"></div>
<div class="photo" style="left:759px;top:1989px;width:296px;height:189px;background:linear-gradient(180deg,#c9d3dc,#8b6f5e 55%,#a9a39c)" role="img" aria-label="Multi-storey building wrapped in scaffolding"></div>
<div class="photo" style="left:452px;top:2188px;width:295px;height:191px;background:linear-gradient(180deg,#9a8b74,#4c4a47 60%,#3a3938)" role="img" aria-label="Workers tying steel reinforcement mesh on a site"></div>
<div class="photo" style="left:759px;top:2188px;width:296px;height:191px;background:linear-gradient(160deg,#e8edf2,#b7c3cf 55%,#8ea2b6)" role="img" aria-label="White curved steel canopy of a modern structure"></div>
<div class="btn" style="left:508px;top:2404px;width:183px;height:42px">View All Projects</div>

<!-- job -->
<section class="abs band job">
  <h2 class="title" style="top:76px">Job Quick Form</h2>
  <div class="rule" style="top:127px"></div>
  <p class="para" style="top:150px;line-height:29px">Maecenas vel tortor accumsan quam varius imperdiet vel eget elit. Aenean facilisis tincidunt lectus, id dictum nisi luctus eget. Vivamus efficitur ex condimentum, malesuada eros eget, feugiat nibh.</p>
  <div class="upload">
    <svg width="22" height="18" viewBox="0 0 22 18"><path d="M1 2h7l2 2h8v3H5L1 16z M5 7h16l-4 10H1z" fill="#888"/></svg>
    Upload File
  </div>
  <div class="btn" style="left:691px;top:237px;width:96px;height:44px;font-size:14px">Send CV</div>
</section>

<!-- partners -->
<h2 class="title" style="top:3015px">Partners and Affiliates</h2>
<div class="rule" style="top:3068px"></div>
<div class="partner" style="left:144px;top:3095px" role="img" aria-label="Partner badge"><i style="width:90px;height:34px;border-radius:4px"></i></div>
<div class="partner" style="left:329px;top:3095px" role="img" aria-label="Partner badge"><i style="width:100px;height:26px;border-radius:4px"></i></div>
<div class="partner" style="left:515px;top:3095px" role="img" aria-label="Partner badge"><i style="width:56px;height:56px;border-radius:50%"></i></div>
<div class="partner" style="left:701px;top:3095px" role="img" aria-label="Partner badge"><i style="width:100px;height:30px;border-radius:4px"></i></div>
<div class="partner" style="left:887px;top:3095px" role="img" aria-label="Partner badge"><i style="width:116px;height:40px;border-radius:4px"></i></div>
<div class="partner" style="left:144px;top:3256px" role="img" aria-label="Partner badge"><i style="width:66px;height:66px;border-radius:50%"></i></div>
<div class="partner" style="left:329px;top:3256px" role="img" aria-label="Partner badge"><i style="width:100px;height:30px;border-radius:4px"></i></div>
<div class="partner" style="left:515px;top:3256px" role="img" aria-label="Partner badge"><i style="width:124px;height:36px;border-radius:4px"></i></div>
<div class="partner" style="left:701px;top:3256px" role="img" aria-label="Partner badge"><i style="width:144px;height:40px;border-radius:4px"></i></div>
<div class="partner" style="left:887px;top:3256px" role="img" aria-label="Partner badge"><i style="width:126px;height:40px;border-radius:4px"></i></div>
<svg class="chev" style="left:53px;top:3232px" width="22" height="32" viewBox="0 0 22 32"><path d="M16 4L6 16l10 12" stroke="#888" stroke-width="4" fill="none"/></svg>
<svg class="chev" style="left:1123px;top:3232px" width="22" height="32" viewBox="0 0 22 32"><path d="M6 4l10 12-10 12" stroke="#888" stroke-width="4" fill="none"/></svg>

<!-- footer -->
<footer class="abs band footer">
  <div class="f-brand">
    <div class="brand-mark" style="width:48px;height:86px"></div>
    <div class="brand-name" style="color:var(--foot-text)">Quarrybend<small>Building Company</small></div>
  </div>
  <div class="f-head" style="left:462px">Menu</div>
  <ul class="f-list" style="left:463px">
    <li>Home</li><li>About Us</li><li>Gallery</li><li>Divisions</li><li>Supplies</li><li>Contact Us</li>
  </ul>
  <div class="f-head" style="left:621px">Contact Info</div>
  <ul class="f-info" style="left:622px">
    <li><b></b>P.O.Box.4410 Jeddah 21300 K.S.A</li>
    <li><b></b>Phone: +966 12 5550148</li>
    <li><b></b>Fax: +966 12 5550193</li>
    <li><b></b>Email : hello@quarrybend.example</li>
  </ul>
  <div class="f-head" style="left:902px">Follow Us On</div>
  <div class="social" style="left:902px" aria-label="Social link"><i></i></div>
  <div class="social" style="left:958px" aria-label="Social link"><i></i></div>
  <div class="social" style="left:1014px" aria-label="Social link"><i></i></div>
  <div class="abs" style="left:144px;top:316px;width:911px;height:1px;background:#3e352e"></div>
  <div class="abs center" style="top:356px;font-size:11px;color:var(--foot-text)">Copyright © 2019 Quarrybend Building Company. All rights reserved.</div>
</footer>

</body>
</html>
```